Stylish, Masculine Design - Men's Clothing

Granary Coat Mart is a 14,000 square foot warehouse outlet store open to the public since 2005. 50+ brands. Well-known designer brand names and private labels. 30-80% off retail everyday. Lowest prices guaranteed. Average suit price $150. Average shirt price $20. One-stop shop shopping. Men's suits, tuxedos, tuxedo rentals, dress shirts, ties, dress shoes, boy's suits and tuxedos, clergy robes, clergy shirts, cologne, loungewear. Slim fits (Prom Dance), business styles, "church" fashion, security-related uniform. Alterations done by expert tailors on premises for an extra charge.
The final design for both business card and logo should portray stylishness and masculinity.
Updates
We will be changing our name. Details below.New name: Warehouse Suit & TuxFormer name: Granary Coat Mart Added Monday, December 26, 2016
Target Market(s)
Gender: 80% Male, 15% Female, 5% Transgender
Location: 80% 10 Mile Radius, 20% >10 Mile Radius
Age: 17-18 (Primarily prom), 18-35 (Primarily Interviews and Weddings), 36-70 (primarily Church and events)
Race: African-American 50%, Latino-American 20%, White 15%, 10% Asian 5% Other
Religions: Christian 50%, 20% Catholic, 10% Mormon, 20% Other/None
Occupation: Local government 40%, Large corporation employee 20%, Small business employee 10%, Small business owner 10%, 20% Unemployed (high school, college)
Education: High School or equivalent 40%, College 30%, Some College 20%, Masters/Doctors 10%
Industry/Entity Type
Retail
Contact Information for Business Card
Name: Peter Olund
Title: Sales Associate
Address: 418 E. Mirabeth Ave. Fernhollow, CA 99047
Phone Number: 555.014.0182
Slogan: Big Racks. Fair Tags, Friendly Fitting Every Day
www.granarycoatmart.example
Logo Text
GCM (Acronym for Granary Coat Mart) or Image
Requirements
Must have
- Easy to read
- Visually appealing

```html
<!DOCTYPE html>
<html lang="en">
<head>
<meta charset="utf-8">
<title>Granary Coat Mart — Business Card</title>
<link rel="stylesheet" href="https://fonts.googleapis.com/css2?family=Oswald:wght@500&family=Arimo:wght@400;700&family=Tinos&display=swap">
<style>
  :root {
    --backdrop: #2b2b2d;
    --card-white: #f7f7f7;
    --brand-red: #d8171f;
    --charcoal: #2e2e2e;
    --ink: #1c1c1c;
    --muted: #4a4a4a;
    --slogan-pink: #f6b9bb;
    --tag-white: #ffffff;
  }
  * { margin: 0; padding: 0; box-sizing: border-box; }
  html, body { width: 1200px; height: 1000px; overflow: hidden; }
  body { background: var(--backdrop); position: relative; }

  .business-card {
    position: absolute; left: 75px; top: 200px;
    width: 1050px; height: 600px;
    background: var(--card-white);
    overflow: hidden;
    box-shadow: 0 10px 30px rgba(0,0,0,.45);
  }
  .card-wave { position: absolute; inset: 0; width: 100%; height: 100%; }

  .brand-name {
    position: absolute; left: 110px; top: 62px;
    display: flex; align-items: center; gap: 18px;
    font-family: 'Oswald', sans-serif; font-weight: 500;
    font-size: 62px; letter-spacing: 2px; text-transform: uppercase;
    color: var(--ink); line-height: 1;
  }
  .brand-mark { width: 22px; height: 22px; background: var(--brand-red); }

  .associate { position: absolute; left: 40px; top: 220px; font-family: 'Arimo', sans-serif; }
  .associate-name { font-size: 46px; font-weight: 700; color: var(--muted); letter-spacing: -0.5px; line-height: 1.1; }
  .associate-name .first { color: var(--brand-red); }
  .associate-title { margin-top: 6px; font-size: 19px; letter-spacing: 7px; color: var(--muted); }

  .address {
    position: absolute; right: 40px; top: 215px; text-align: right;
    font-family: 'Arimo', sans-serif; font-style: normal;
    font-size: 20px; color: var(--muted); line-height: 1.35;
  }
  .address-label { color: var(--brand-red); font-weight: 700; font-size: 22px; margin-bottom: 4px; }

  .contact-list { position: absolute; left: 560px; top: 432px; list-style: none; }
  .contact-item {
    display: flex; align-items: center; gap: 16px; margin-bottom: 22px;
    font-family: 'Tinos', serif; font-size: 30px; color: var(--tag-white); letter-spacing: 1px;
    line-height: 1.1;
  }
  .contact-item.web { font-family: 'Arimo', sans-serif; font-size: 23px; letter-spacing: 1.5px; }
  .contact-tag {
    flex: none;
    width: 34px; height: 28px; border-radius: 4px; background: var(--tag-white);
    color: var(--brand-red); font-family: 'Arimo', sans-serif; font-size: 17px; font-weight: 700;
    letter-spacing: 0;
    display: flex; align-items: center; justify-content: center;
  }

  .slogan {
    position: absolute; left: 40px; bottom: 40px;
    font-family: 'Arimo', sans-serif; font-size: 19px; letter-spacing: 1px; color: var(--slogan-pink);
  }
</style>
</head>
<body>
  <article class="business-card">
    <svg class="card-wave" viewBox="0 0 1050 600" preserveAspectRatio="none" aria-hidden="true">
      <path d="M0 318 C160 340 330 390 470 388 C640 386 800 300 1050 350 L1050 600 L0 600 Z" fill="var(--charcoal)"/>
      <path d="M0 348 C170 372 340 408 480 404 C650 398 820 330 1050 372 L1050 600 L0 600 Z" fill="var(--card-white)"/>
      <path d="M0 362 C180 384 350 416 500 410 C680 402 840 340 1050 388 L1050 600 L0 600 Z" fill="var(--brand-red)"/>
    </svg>

    <div class="brand-name"><span class="brand-mark"></span>Granary Coat Mart</div>

    <div class="associate">
      <h1 class="associate-name"><span class="first">Peter</span>Olund</h1>
      <p class="associate-title">Sales Associate</p>
    </div>

    <address class="address">
      <div class="address-label">Address</div>
      418 E. Mirabeth Ave.<br>Fernhollow, CA 99047
    </address>

    <ul class="contact-list">
      <li class="contact-item"><span class="contact-tag">M</span>555.014.0182</li>
      <li class="contact-item web"><span class="contact-tag">W</span>www.granarycoatmart.example</li>
    </ul>

    <p class="slogan">Big Racks. Fair Tags, Friendly Fitting Every Day</p>
  </article>
</body>
</html>
```